Billboard design for a dental office. 10 feet x 20 feet in size.

We need a BILLBOARD design for our dental office. Something creative, yet simple that will grab the attention of people driving by and guide them to our office and webpage. The billboards will be in high traffic areas and must be concise and grab the attention of people driving by.
An attractive or creative image is important, as there are many other billboards along these stretches of road, so we need to stand out. You can get a feel for the office by visiting www.brookmarlowdental.example. We are a dental office that offers dentistry for the kids, adults and seniors. our main goal is to let people know we are accepting new patients and to have them visit our website and office.

Target Market(s)

Families looking for a Dentist.
Business people travelling to work and looking for a dentist in the downtown core.

Industry/Entity Type

Dental Clinic

Font styles to use
Serif

Colors
fbf289
fdf9cf

Requirements
Must have
• 1. Simple Design to grab attention of people driving by.
• 2. Website name www.BrookMarlowDental.example
• 3. Yellow and Black as main colours.
• 4. Quote: "Smile, It's contagious"
Nice to have
• One Margin can list our services:
• Dentistry for the entire family
• Hygiene and Whitening
• Dentures
• Fillings and Crowns
• Implants
• "Kids and Cowards welcome"
Should not have
• Shouldn't have too much information or be overwhelming. People are driving by fairly quickly, so the billboard has to be simple, creative and grab their attention.

```html
<!DOCTYPE html>
<html lang="en">
<head>
<meta charset="utf-8">
<title>Brook Marlow Dental – Billboard</title>
<link href="https://fonts.googleapis.com/css2?family=Dosis:wght@500;600&family=Open+Sans:wght@300;400;700&family=Gochi+Hand&display=swap" rel="stylesheet">
<style>
  :root {
    --board-warm: #e6df9e;
    --board-pale: #f7f5e8;
    --ink: #1c1a14;
    --band: #1e1d1a;
    --band-text: #e9e7df;
    --band-muted: #c9c7bf;
    --accent-yellow: #fbf289;
    --accent-gold: #e9dc5c;
  }
  * { box-sizing: border-box; margin: 0; padding: 0; }
  html, body { width: 1200px; height: 600px; overflow: hidden; background: #ffffff; }
  .billboard {
    position: relative;
    width: 1200px;
    height: 600px;
    overflow: hidden;
    background: linear-gradient(90deg, var(--board-warm) 0%, #ece7b8 40%, var(--board-pale) 100%);
    color: var(--ink);
  }
  .services {
    position: absolute;
    left: 88px;
    top: 72px;
    list-style: none;
    font-family: "Dosis", "Open Sans", sans-serif;
    font-weight: 500;
    font-size: 37px;
    line-height: 1;
  }
  .services li {
    position: relative;
    padding-left: 30px;
    margin-bottom: 29px;
  }
  .services li::before {
    content: "";
    position: absolute;
    left: 0;
    top: 13px;
    width: 8px;
    height: 8px;
    border-radius: 50%;
    background: var(--ink);
  }
  .welcome {
    position: absolute;
    left: 88px;
    top: 374px;
    font-family: "Dosis", "Open Sans", sans-serif;
    font-weight: 500;
    font-size: 36px;
    letter-spacing: 0.5px;
    text-transform: uppercase;
  }
  .smile-art {
    position: absolute;
    left: 560px;
    top: 140px;
    width: 350px;
    height: 280px;
    border-radius: 48% 48% 50% 50%;
    background: radial-gradient(ellipse at 50% 60%, #ffffff 0%, #f3f1e2 55%, rgba(243,241,226,0) 75%);
  }
  .quote {
    position: absolute;
    left: 850px;
    top: 300px;
    font-family: "Gochi Hand", cursive;
    font-size: 52px;
    line-height: 1.05;
    text-align: center;
    color: var(--ink);
    transform: rotate(-16deg);
  }
  .band {
    position: absolute;
    left: 0;
    right: 0;
    bottom: 0;
    height: 168px;
    background: var(--band);
    text-align: center;
    font-family: "Open Sans", sans-serif;
  }
  .website {
    margin-top: 24px;
    font-size: 44px;
    font-weight: 700;
    letter-spacing: 1px;
    color: var(--band-text);
  }
  .website .tld { color: var(--accent-gold); }
  .tagline {
    margin-top: 8px;
    font-size: 32px;
    font-weight: 300;
    letter-spacing: 2px;
    color: var(--band-muted);
  }
  .tagline strong { font-weight: 700; color: var(--accent-yellow); }
</style>
</head>
<body>
  <main class="billboard">
    <ul class="services">
      <li>Dentistry for the entire family.</li>
      <li>Hygiene and Whitening.</li>
      <li>Dentures and Implants.</li>
      <li>Fillings and Crowns.</li>
    </ul>
    <p class="welcome">Kids and Cowards Welcome</p>

    <div class="smile-art" role="img" aria-label="Illustration of a large, cheerful winking smile with white teeth"></div>

    <p class="quote">Smile, It's<br>contagious!</p>

    <footer class="band">
      <p class="website">BrookMarlowDental<span class="tld">.example</span></p>
      <p class="tagline">Family Dentistry <strong>in the Heart of</strong> Downtown Marlow Falls</p>
    </footer>
  </main>
</body>
</html>
```